Visitenkarten-Design für italienisches Küchenschiff
Zielgruppe
Restaurantschiff Ilvora
Aufgabenstellung
Wir sind ein italienische Küche Schiff auf der Binnenalster in Hamburg und wollen den schönen Blick und gerne auch die italienischen Farben widerspiegeln...ich brauche das einmal neutral für den normalen Gast....und würde das denn..wenn es denn gut wird...auch gerne individell mit m e i n e r Tel Nr und auch für meine führenden Mitarbeiter personalisieren...aber...zuerst natürlich das neutrale...dazu schicke ich die alte Karte mit dem auch alten Logo was nicht unbedingt verwendet werden muss...

```html
<!DOCTYPE html>
<html lang="de">
<head>
<meta charset="utf-8">
<title>Restaurantschiff Ilvora – Visitenkarten</title>
<link rel="stylesheet" href="https://fonts.googleapis.com/css2?family=Dosis:wght@200;300&display=swap">
<style>
  :root {
    --stage: #4a4a4a;
    --card-warm: #4a4546;
    --card-dark: #373737;
    --strip: #3f3b3c;
    --taupe: #9d9081;
    --taupe-light: #a89d91;
    --it-green: #0f9a50;
    --it-white: #ffffff;
    --it-red: #a83236;
    --map-white: #fbfaf7;
    --map-light: #e4dccd;
    --map-dark: #b0a695;
    --photo-day: #5d7893;
    --photo-red: #8e3a3c;
    --photo-dusk: #7c6a7e;
    --photo-night: #2c2a33;
  }
  html, body {
    margin: 0; padding: 0;
    width: 1200px; height: 1200px;
    overflow: hidden;
    background: var(--stage);
    font-family: "Dosis", sans-serif;
    font-weight: 300;
  }
  .canvas { position: relative; width: 1200px; height: 1200px; }

  .card {
    position: absolute;
    width: 510px; height: 328px;
    overflow: hidden;
    background: var(--card-bg);
    box-shadow: 3px 4px 6px rgba(0,0,0,.35);
  }
  .variant-warm { --card-bg: var(--card-warm); }
  .variant-dark { --card-bg: var(--card-dark); }

  /* Front */
  .flag-strip {
    position: absolute; left: 0; top: 0; width: 14px; height: 100%;
    background: linear-gradient(var(--it-green) 0 33.3%, var(--it-white) 33.3% 66.6%, var(--it-red) 66.6% 100%);
  }
  .shade-strip { position: absolute; left: 14px; top: 0; width: 19px; height: 100%; background: var(--strip); }
  .map-area {
    position: absolute; left: 33px; top: 0; width: 210px; height: 100%;
    background:
      radial-gradient(ellipse 55% 50% at 58% 52%, var(--map-dark) 0%, var(--map-dark) 45%, rgba(176,166,149,0) 75%),
      linear-gradient(135deg, var(--map-white) 0%, var(--map-light) 40%, var(--map-light) 65%, var(--map-white) 100%);
  }
  .front-text { position: absolute; left: 271px; top: 0; right: 0; color: var(--taupe); }
  .brand-mark {
    position: absolute; left: 112px; top: 24px;
    width: 76px; height: 76px;
    border: 1.5px solid var(--taupe); border-radius: 50%;
  }
  .brand-name {
    position: absolute; top: 86px; left: 0;
    font-size: 40px; letter-spacing: 2px; line-height: 1; font-weight: 300;
  }
  .brand-tagline {
    position: absolute; top: 128px; left: 0;
    font-size: 17px; letter-spacing: 5.6px; line-height: 1; font-weight: 300;
  }
  .contact-block { position: absolute; top: 160px; left: 0; font-size: 17px; line-height: 20px; white-space: nowrap; }
  .contact-block p { margin: 0; }
  .contact-block .label-gap { margin-top: 5px; }
  .contact-block .key { display: inline-block; width: 33px; }

  /* Back */
  .photo { position: absolute; left: 22px; width: 211px; }
  .photo-interior {
    top: 20px; height: 129px;
    background: linear-gradient(180deg, #a87a45 0 9%, var(--photo-day) 9% 55%, var(--photo-red) 55% 75%, #efefef 75% 100%);
  }
  .photo-skyline {
    top: 163px; height: 125px;
    background: linear-gradient(180deg, var(--photo-dusk) 0%, #5b5161 55%, #7a6b55 72%, var(--photo-night) 80%, #3a3540 100%);
  }
  .back-text { position: absolute; left: 257px; top: 0; right: 0; color: var(--taupe-light); white-space: nowrap; }
  .back-text h2 { position: absolute; left: 0; margin: 0; font-size: 22px; font-weight: 300; line-height: 1; }
  .back-text p { position: absolute; margin: 0; font-size: 17px; line-height: 1; }
  .hours-title { top: 45px; }
  .hours-days { top: 74px; left: 0; }
  .hours-time { top: 74px; left: 134px; }
  .hours-kitchen { top: 100px; left: 113px; }
  .divider { position: absolute; left: 309px; top: 155px; width: 122px; height: 1px; background: var(--taupe); opacity: .7; }
  .reserve-title { top: 178px; }
  .reserve-line-1 { top: 207px; left: 0; }
  .reserve-line-2 { top: 228px; left: 0; }
  .reserve-line-3 { top: 250px; left: 0; }
  .flag-bar {
    position: absolute; left: 0; top: 301px; width: 100%; height: 9px;
    background: linear-gradient(90deg, var(--it-green) 0 33.3%, var(--it-white) 33.3% 66.6%, var(--it-red) 66.6% 100%);
  }
</style>
</head>
<body>
<div class="canvas">

  <section class="card card-front variant-warm" style="left:61px; top:180px;">
    <div class="flag-strip"></div>
    <div class="shade-strip"></div>
    <div class="map-area" role="img" aria-label="Lageplan mit Binnenalster, umliegenden Straßen und Anlegestelle des Schiffes"></div>
    <div class="front-text">
      <div class="brand-mark"></div>
      <div class="brand-name">ILVORA</div>
      <div class="brand-tagline">Schiffsrestaurant</div>
      <div class="contact-block">
        <p>Kaimauer 7b (Wasserseite)</p>
        <p>20099 Hamburg</p>
        <p class="label-gap">Kontakt</p>
        <p><span class="key">Tel:</span>+49 040 / 55 18 40</p>
        <p><span class="key">Fax:</span>+49 040 / 55 18 41</p>
        <p>www.ilvora-schiff.de</p>
        <p>E-Mail: info@ilvora-schiff.de</p>
      </div>
    </div>
  </section>

  <section class="card card-back variant-warm" style="left:628px; top:180px;">
    <div class="photo photo-interior" role="img" aria-label="Gedeckte Tische im Salon des Schiffes mit Panoramafenstern zur Alster"></div>
    <div class="photo photo-skyline" role="img" aria-label="Abendliche Stadtsilhouette mit Lichtern, die sich im Wasser spiegeln"></div>
    <div class="back-text">
      <h2 class="hours-title">Öffnungszeiten</h2>
      <p class="hours-days">Montag - Sonntag</p>
      <p class="hours-time">12:00 - 23:00</p>
      <p class="hours-kitchen">Küche bis 22:00</p>
      <h2 class="reserve-title">Reservierungen</h2>
      <p class="reserve-line-1">Wir freuen uns auf Ihren Anruf oder</p>
      <p class="reserve-line-2">eine E-Mail:</p>
      <p class="reserve-line-3">reservierung@ilvora-schiff.de</p>
    </div>
    <div class="divider"></div>
    <div class="flag-bar"></div>
  </section>

  <section class="card card-front variant-dark" style="left:65px; top:666px;">
    <div class="flag-strip"></div>
    <div class="shade-strip"></div>
    <div class="map-area" role="img" aria-label="Lageplan mit Binnenalster, umliegenden Straßen und Anlegestelle des Schiffes"></div>
    <div class="front-text">
      <div class="brand-mark"></div>
      <div class="brand-name">ILVORA</div>
      <div class="brand-tagline">Schiffsrestaurant</div>
      <div class="contact-block">
        <p>Kaimauer 7b (Wasserseite)</p>
        <p>20099 Hamburg</p>
        <p class="label-gap">Kontakt</p>
        <p><span class="key">Tel:</span>+49 040 / 55 18 40</p>
        <p><span class="key">Fax:</span>+49 040 / 55 18 41</p>
        <p>www.ilvora-schiff.de</p>
        <p>E-Mail: info@ilvora-schiff.de</p>
      </div>
    </div>
  </section>

  <section class="card card-back variant-dark" style="left:633px; top:667px;">
    <div class="photo photo-interior" role="img" aria-label="Gedeckte Tische im Salon des Schiffes mit Panoramafenstern zur Alster"></div>
    <div class="photo photo-skyline" role="img" aria-label="Abendliche Stadtsilhouette mit Lichtern, die sich im Wasser spiegeln"></div>
    <div class="back-text">
      <h2 class="hours-title">Öffnungszeiten</h2>
      <p class="hours-days">Montag - Sonntag</p>
      <p class="hours-time">12:00 - 23:00</p>
      <p class="hours-kitchen">Küche bis 22:00</p>
      <h2 class="reserve-title">Reservierungen</h2>
      <p class="reserve-line-1">Wir freuen uns auf Ihren Anruf oder</p>
      <p class="reserve-line-2">eine E-Mail:</p>
      <p class="reserve-line-3">reservierung@ilvora-schiff.de</p>
    </div>
    <div class="divider"></div>
    <div class="flag-bar"></div>
  </section>

</div>
</body>
</html>
```